Marlow Hire Business Card for recruitment company

We are looking for a Business Card Design that incorporates our personal details and our busines name and logo. We are a specialized search consultancy that recruit Property and Construction professionals.
We would like a business card that stands out and is appealing to the Construction and Property industry as well.

Target Market(s)

people in the construction and property industry

Contact Information for Business Card

Business Name and logo

Font styles to use
Serif

Colors
0094D4
00A9DD
6FCCEA
C7EBF8
E9F6FB

Requirements
Must have
• Business name and logo as well as contact details
Should not have
• No photos of us please

```html
<!DOCTYPE html>
<html lang="en">
<head>
<meta charset="utf-8">
<title>Marlow Hire – Business Card</title>
<link rel="stylesheet" href="https://fonts.googleapis.com/css2?family=Lora:wght@400;500&family=Lato:wght@400&display=swap">
<style>
  :root {
    --bg: #4d4d4f;
    --card: #ffffff;
    --ink: #3a4450;
    --ink-soft: #4c5560;
    --blue: #0094d4;
    --blue-bright: #00a9dd;
    --blue-mid: #6fccea;
    --blue-pale: #c7ebf8;
    --blue-mist: #e9f6fb;
  }
  * { margin: 0; padding: 0; box-sizing: border-box; }
  html, body { width: 1200px; height: 899px; overflow: hidden; background: var(--bg); }
  .canvas { position: relative; width: 1200px; height: 899px; }

  .card {
    position: absolute;
    width: 500px;
    height: 286px;
    background: var(--card);
    overflow: hidden;
    box-shadow: 0 12px 28px rgba(0,0,0,.35);
  }
  .card--front { left: 70px; top: 120px; }
  .card--back  { left: 630px; top: 490px; }

  .card__texture {
    position: absolute; inset: 0;
    background: linear-gradient(160deg, var(--card) 20%, var(--blue-mist) 55%, var(--blue-pale) 100%);
  }
  .card__edge {
    position: absolute; left: 0; right: 0; bottom: 0; height: 3px;
    background: var(--blue-mid);
  }

  .rule { position: absolute; height: 2px; background: var(--blue-bright); }

  .brand-name {
    position: absolute;
    font-family: "Lora", serif;
    font-weight: 400;
    letter-spacing: 2px;
    text-transform: uppercase;
    color: var(--ink);
    white-space: nowrap;
  }

  /* front */
  .card--front .rule--left  { left: 0; top: 131px; width: 170px; }
  .card--front .rule--right { left: 372px; top: 131px; right: 0; }
  .card--front .brand-name { left: 182px; top: 117px; font-size: 24px; }

  /* back */
  .card--back .brand-name { right: 46px; top: 62px; font-size: 24px; }
  .card--back .rule--main { left: 210px; right: 0; top: 109px; }

  .person { position: absolute; left: 28px; top: 97px; font-family: "Lora", serif; color: var(--ink); }
  .person__name { font-size: 18px; letter-spacing: .5px; text-transform: uppercase; line-height: 22px; }
  .person__role { font-size: 14px; color: var(--ink-soft); line-height: 18px; }
  .person__underline { width: 58px; height: 2px; background: var(--blue-bright); margin-top: 4px; }

  .contact {
    position: absolute;
    font-family: "Lato", sans-serif;
    font-size: 10.5px;
    color: var(--ink);
    line-height: 16px;
  }
  .contact__row { display: flex; align-items: center; gap: 6px; }
  .contact--address { left: 28px; top: 214px; }
  .contact--lines { left: 200px; top: 206px; }
  .contact--web { right: 22px; top: 206px; }
  .contact--lines .contact__row + .contact__row { margin-top: 6px; }

  .icon { width: 14px; height: 14px; flex: none; display: block; }
</style>
</head>
<body>
<main class="canvas">

  <section class="card card--front" aria-label="Business card front">
    <div class="card__texture" role="img" aria-label="Soft pale blue faceted background pattern"></div>
    <div class="rule rule--left"></div>
    <div class="brand-name">Marlow Hire</div>
    <div class="rule rule--right"></div>
    <div class="card__edge"></div>
  </section>

  <section class="card card--back" aria-label="Business card back">
    <div class="card__texture" role="img" aria-label="Soft pale blue faceted background pattern"></div>
    <div class="brand-name">Marlow Hire</div>
    <div class="rule rule--main"></div>

    <div class="person">
      <div class="person__name">Daniel J. Hartley</div>
      <div class="person__role">Managing Director</div>
      <div class="person__underline"></div>
    </div>

    <div class="contact contact--address">
      <div class="contact__row">
        <div>2173 Eastfield Avenue<br>Portland, OR 97205</div>
        <svg class="icon" viewBox="0 0 14 14"><rect width="14" height="14" rx="2" fill="#3a4450"/><path d="M7 3a2.6 2.6 0 0 0-2.6 2.6C4.4 7.6 7 11 7 11s2.6-3.4 2.6-5.4A2.6 2.6 0 0 0 7 3z" fill="#fff"/><circle cx="7" cy="5.6" r="1" fill="#3a4450"/></svg>
      </div>
    </div>

    <div class="contact contact--lines">
      <div class="contact__row">
        <span>+00 987 654 32</span>
        <svg class="icon" viewBox="0 0 14 14"><rect width="14" height="14" rx="2" fill="#00a9dd"/><path d="M4.3 3.5l1.6-.3.8 2-1 .8a6 6 0 0 0 2.3 2.3l.8-1 2 .8-.3 1.6c-3.4.3-6.5-2.8-6.2-6.2z" fill="#fff"/></svg>
      </div>
      <div class="contact__row">
        <span>contact@marlowhire.com</span>
        <svg class="icon" viewBox="0 0 14 14"><rect width="14" height="14" rx="2" fill="#00a9dd"/><rect x="3" y="4.2" width="8" height="5.6" fill="#fff"/><path d="M3 4.2l4 3.2 4-3.2" fill="none" stroke="#00a9dd" stroke-width=".9"/></svg>
      </div>
    </div>

    <div class="contact contact--web">
      <div class="contact__row">
        <span>www.marlowhire.com</span>
        <svg class="icon" viewBox="0 0 14 14"><rect width="14" height="14" rx="2" fill="#00a9dd"/><path d="M4 4l6 2.3-2.4.9L9.8 9.4l-.8.8-2.2-2.2-.9 2.4z" fill="#fff"/></svg>
      </div>
    </div>

    <div class="card__edge"></div>
  </section>

</main>
</body>
</html>
```